Bref créative
Brightwave IT Business cards
Professional
Kenneth Darrow
Chief Information Officer
248 Maple Hollow Rd
KDarrow@BrightwaveIT.example
www.brightwaveit.example
IT managed services
Managed backups
Web Hosting
Email Hosting
Spam Filtering
Networking
Structured Cabling
Project Planning
Colocation Services

```html
<!DOCTYPE html>
<html lang="en">
<head>
<meta charset="utf-8">
<title>Brightwave IT — Business Cards</title>
<link rel="stylesheet" href="https://fonts.googleapis.com/css2?family=Open+Sans:ital,wght@0,400;0,600;0,700;1,600&display=swap">
<style>
  :root {
    --page-bg: #ffffff;
    --card-white: #ffffff;
    --card-edge: #d4d8de;
    --brand-blue: #1f5fae;
    --panel-top: #2a72c9;
    --panel-mid: #1652a8;
    --panel-bottom: #0c3c8a;
    --band-grey: #d3d7de;
    --band-light: #f2f3f5;
    --band-dark: #c5cad2;
    --text-white: #ffffff;
    --text-soft: #dbe7f7;
  }
  * { margin: 0; padding: 0; box-sizing: border-box; }
  html, body {
    width: 1200px; height: 533px; overflow: hidden;
    background: var(--page-bg);
    font-family: "Open Sans", Arial, sans-serif;
  }
  .canvas { position: relative; width: 1200px; height: 533px; }
  .card {
    position: absolute; top: 120px; width: 497px; height: 293px;
    background: var(--card-white);
    box-shadow: 0 0 0 1px var(--card-edge);
    overflow: hidden;
  }
  .card--front { left: 89px; }
  .card--back { left: 614px; }

  .brand {
    position: absolute; left: 70px; top: 40px;
    display: flex; align-items: center; gap: 14px;
  }
  .brand__dot {
    width: 46px; height: 46px; border-radius: 50%;
    background: var(--brand-blue);
  }
  .brand__name {
    font-size: 40px; font-weight: 700; color: var(--brand-blue);
    letter-spacing: 0.5px; line-height: 1;
  }

  .front-panel {
    position: absolute; left: 0; right: 0; top: 118px; bottom: 0;
    background: linear-gradient(to bottom, var(--band-light), var(--band-dark)) top / 100% 14px no-repeat,
                linear-gradient(135deg, var(--panel-top), var(--panel-mid) 55%, var(--panel-bottom));
  }

  .contact {
    position: absolute; left: 9px; top: 150px; color: var(--text-white);
  }
  .contact__name { font-size: 17px; font-weight: 600; line-height: 1.2; }
  .contact__title { font-size: 13px; font-weight: 600; font-style: italic; margin-top: 2px; }
  .contact__details { margin-top: 22px; font-size: 11px; line-height: 15px; border-collapse: collapse; }
  .contact__details th { font-weight: 700; text-align: left; padding-right: 8px; }
  .contact__details td { font-weight: 400; }

  .services {
    position: absolute; left: 318px; top: 150px; list-style: none;
    color: var(--text-white); font-size: 10.5px; line-height: 14.5px;
  }
  .services li::before { content: "» "; color: var(--text-soft); }

  .back-band {
    position: absolute; left: 0; right: 0; bottom: 0; height: 40px;
    background: linear-gradient(var(--band-grey), var(--band-grey)) top / 100% 9px no-repeat,
                linear-gradient(to right, var(--panel-top), var(--panel-bottom));
  }
</style>
</head>
<body>
<div class="canvas">
  <section class="card card--front" aria-label="Business card front">
    <div class="brand">
      <span class="brand__dot"></span>
      <span class="brand__name">Brightwave IT</span>
    </div>

    <div class="front-panel"></div>

    <div class="contact">
      <p class="contact__name">Kenneth Darrow</p>
      <p class="contact__title">Chief Information Officer</p>
      <table class="contact__details">
        <tr><th>Address</th><td>: 248 Maple Hollow Rd</td></tr>
        <tr><th>Phone</th><td>: 512 555-0147</td></tr>
        <tr><th>Email</th><td>: KDarrow@BrightwaveIT.example</td></tr>
        <tr><th>Website</th><td>: www.brightwaveit.example</td></tr>
      </table>
    </div>

    <ul class="services">
      <li>IT managed services</li>
      <li>Managed backups</li>
      <li>Web Hosting</li>
      <li>Email Hosting</li>
      <li>Spam Filtering</li>
      <li>Networking</li>
      <li>Structured Cabling</li>
      <li>Project Planning</li>
      <li>Colocation Services</li>
    </ul>
  </section>

  <section class="card card--back" aria-label="Business card back">
    <div class="back-band"></div>
  </section>
</div>
</body>
</html>
```